Event flyer for Sunday night Youth Group

Need a 4 x 6 or 5 x 7 flyer for a new youth group starting on April 14. The youth group is for students in middle school and high school so it needs to look fun and cool, but not childish. I prefer it not to include pictures of people unless it's so obscure you can't really see their faces. I've uploaded some pictures of flyers I like. I've also attached a couple versions of our logo to use on the flyer.
Information the flyer needs to include:
Youth Group
Sundays, 6-8pm (beginning April 14)
Location: Merriwick's - 4219 Hollowfern Ln S, Keizer, 97418
There will be dinner, games, friends, and a message.
Target Market(s)
Youth ages 13-18
Industry/Entity Type
Church
Colors
Designer to choose colors to be used in the design.
Look and feel

```html
<!DOCTYPE html>
<html lang="en">
<head>
<meta charset="utf-8">
<title>Youth Group Flyer</title>
<link href="https://fonts.googleapis.com/css2?family=Anton&family=Montserrat:wght@500;600;700&family=Yellowtail&display=swap" rel="stylesheet">
<style>
  :root {
    --yellow: #ffd60a;
    --navy: #1d3a9a;
    --ink: #1b2440;
    --mist: #e9e8e2;
    --stage: #d9d7cf;
    --paper: #f6f4ec;
  }
  * { margin: 0; padding: 0; box-sizing: border-box; }
  html, body { width: 1200px; height: 1200px; overflow: hidden; }
  body {
    background: var(--stage);
    font-family: "Montserrat", sans-serif;
    color: var(--ink);
    position: relative;
  }
  .flyer {
    position: absolute;
    left: 200px; top: 40px;
    width: 800px; height: 1120px;
    overflow: hidden;
    background: linear-gradient(160deg, #f3f2ee 0%, var(--mist) 45%, #f0e7a8 100%);
    box-shadow: 0 10px 40px rgba(0,0,0,.18);
  }
  .photo-bible {
    position: absolute; left: 0; top: 90px; width: 250px; height: 470px;
    background: linear-gradient(180deg, #8f8c82 0%, #cfcbbf 60%, #e8e4d6 100%);
  }
  .photo-sky {
    position: absolute; left: 250px; top: 0; width: 550px; height: 560px;
    background: radial-gradient(ellipse at 45% 30%, #ffffff 0%, #d8d6cf 45%, #8f8d84 100%);
  }
  .wash {
    position: absolute; left: 0; top: 0; width: 800px; height: 620px;
    background: linear-gradient(200deg, rgba(255,214,10,.35) 0%, rgba(255,214,10,0) 45%, rgba(255,214,10,.25) 100%);
  }
  .brand-tag {
    position: absolute; left: 0; top: 150px;
    height: 110px; width: 300px;
    background: var(--yellow);
    clip-path: polygon(0 0, 100% 0, 88% 100%, 0 100%);
    display: flex; align-items: center; gap: 14px; padding-left: 28px;
  }
  .brand-mark { width: 26px; height: 26px; background: var(--ink); }
  .brand-name {
    font-weight: 600; font-size: 19px; line-height: 1.1; letter-spacing: .5px;
    color: var(--ink); text-transform: uppercase;
  }
  .torn-paper { position: absolute; left: 0; top: 560px; width: 800px; height: 560px; }
  .title-youth {
    position: absolute; left: 40px; top: 330px;
    font-family: "Anton", sans-serif; font-size: 290px; line-height: 1; font-weight: 400;
    color: var(--yellow); letter-spacing: 2px;
    text-shadow: 0 6px 14px rgba(0,0,0,.22);
  }
  .title-group {
    position: absolute; left: 380px; top: 540px;
    font-family: "Yellowtail", cursive; font-size: 150px; line-height: 1;
    color: var(--navy); white-space: nowrap;
    text-shadow: 3px 3px 0 #fff;
  }
  .tag {
    display: inline-block; background: var(--yellow);
    color: var(--ink); font-weight: 600; padding: 4px 12px;
  }
  .when { position: absolute; left: 50px; top: 760px; }
  .when .tag-day { font-size: 30px; }
  .when .time { font-size: 104px; font-weight: 500; color: var(--ink); line-height: 1; margin: 4px 0 8px; letter-spacing: -1px; }
  .when .tag-start { font-size: 20px; }
  .divider { position: absolute; left: 440px; top: 730px; width: 3px; height: 280px; background: var(--yellow); }
  .where { position: absolute; left: 470px; top: 720px; }
  .where .tag-loc { font-size: 30px; display: inline-flex; align-items: center; gap: 6px; }
  .where address { font-style: normal; font-size: 24px; font-weight: 500; line-height: 1.25; margin-top: 10px; color: var(--ink); }
  .who { position: absolute; left: 470px; top: 900px; width: 310px; }
  .who .tag-age { font-size: 20px; }
  .who p { font-size: 20px; font-weight: 500; line-height: 1.3; margin-top: 8px; }
  .icon-row { position: absolute; left: 470px; top: 1040px; display: flex; gap: 20px; align-items: center; }
  .icon-row svg { width: 44px; height: 44px; stroke: var(--navy); fill: none; stroke-width: 2.4; stroke-linecap: round; stroke-linejoin: round; }
  .icon-sep { width: 2px; height: 40px; background: var(--yellow); }
</style>
</head>
<body>
  <article class="flyer">
    <div class="photo-sky" role="img" aria-label="Misty sky with a robed figure and a stone cross, faces obscured"></div>
    <div class="photo-bible" role="img" aria-label="Hands holding an open Bible in muted tones"></div>
    <div class="wash"></div>

    <div class="brand-tag">
      <span class="brand-mark"></span>
      <span class="brand-name">Wayfarer<br>Fellowship</span>
    </div>

    <svg class="torn-paper" viewBox="0 0 800 560" preserveAspectRatio="none">
      <defs>
        <linearGradient id="paperFade" x1="0" y1="0" x2="1" y2="1">
          <stop offset="0" stop-color="#ffd60a" stop-opacity="0"/>
          <stop offset="1" stop-color="#ffd60a" stop-opacity=".35"/>
        </linearGradient>
      </defs>
      <path d="M0 60 L60 40 L120 70 L190 35 L260 62 L330 30 L400 58 L470 28 L540 55 L610 25 L680 50 L740 20 L800 45 L800 560 L0 560 Z" fill="#f6f4ec"/>
      <path d="M0 60 L60 40 L120 70 L190 35 L260 62 L330 30 L400 58 L470 28 L540 55 L610 25 L680 50 L740 20 L800 45" fill="none" stroke="#ffffff" stroke-width="6"/>
      <rect x="0" y="300" width="800" height="260" fill="url(#paperFade)"/>
    </svg>

    <h1 class="title-youth">YOUTH</h1>
    <div class="title-group">Group</div>

    <section class="where">
      <span class="tag tag-loc">Location
        <svg width="24" height="24" viewBox="0 0 24 24" fill="none" stroke="#1d3a9a" stroke-width="2"><path d="M12 21s-7-6.5-7-12a7 7 0 0 1 14 0c0 5.5-7 12-7 12z"/><circle cx="12" cy="9" r="2.5"/></svg>
      </span>
      <address>Merriwick's - 4219<br>Hollowfern Ln S,<br>Keizer, 97418</address>
    </section>

    <div class="divider"></div>

    <section class="when">
      <span class="tag tag-day">Sundays</span>
      <div class="time">6-8pm</div>
      <span class="tag tag-start">(beginning April 14)</span>
    </section>

    <section class="who">
      <span class="tag tag-age">Youth ages 13-18</span>
      <p>There will be dinner, games, friends, and a message.</p>
    </section>

    <div class="icon-row">
      <svg viewBox="0 0 48 48" aria-label="Dinner"><path d="M6 36h36"/><path d="M10 36a14 14 0 0 1 28 0"/><path d="M24 18v-4"/><circle cx="24" cy="12" r="2"/><path d="M8 40h32"/></svg>
      <span class="icon-sep"></span>
      <svg viewBox="0 0 48 48" aria-label="Friends"><path d="M10 42V26l8-10 4 4-4 8"/><path d="M38 42V26l-8-10-4 4 4 8"/><path d="M6 12l3 3M24 6v4M42 12l-3 3"/></svg>
      <span class="icon-sep"></span>
      <svg viewBox="0 0 48 48" aria-label="Games"><path d="M14 16h20a8 8 0 0 1 8 8l1 8a5 5 0 0 1-9 3l-3-4H17l-3 4a5 5 0 0 1-9-3l1-8a8 8 0 0 1 8-8z"/><path d="M15 22v6M12 25h6"/><circle cx="32" cy="23" r="1.2"/><circle cx="35" cy="27" r="1.2"/></svg>
      <span class="icon-sep"></span>
      <svg viewBox="0 0 48 48" aria-label="Message"><path d="M24 8c10 0 18 6.5 18 15s-8 15-18 15c-2.5 0-5-.4-7-1.2L8 40l2.5-7.5C7.7 30 6 26.7 6 23 6 14.5 14 8 24 8z"/><circle cx="17" cy="23" r="1.2"/><circle cx="24" cy="23" r="1.2"/><circle cx="31" cy="23" r="1.2"/></svg>
    </div>
  </article>
</body>
</html>
```